BRIVETTA Need a luxury modern business card designed.

Need a luxury modern business card designed. refer to the uploaded files for the company name and logo in the zip file under source files. i will making my descion on monday. so please send in before then so if we need to edit we will have the time. we have a trade show coming up and im on a deadline for printer.

Target Market(s)

high end clients

Contact Information for Business Card

Company nAme and logo. Calvin Moross Co-Founder / Project Manager Office # 416-555-7391 Cell # 416-555-0186 BRIVETTA.CA Calvin@brivetta.ca

Font styles to use
Other font styles liked:
• Modern

Requirements
Must have
• Company name and logo, contact info, using the black, gold and white color scheme.

```html
<!DOCTYPE html>
<html lang="en">
<head>
<meta charset="utf-8">
<title>BRIVETTA Business Card</title>
<link rel="stylesheet" href="https://fonts.googleapis.com/css2?family=Work+Sans:wght@300;400;600&display=swap">
<style>
  :root {
    --backdrop: #1c1c1c;
    --card: #1a1a1a;
    --card-edge: #232323;
    --gold: #b3a37a;
    --white: #f4f4f2;
    --muted: #8c8c8c;
  }
  * { box-sizing: border-box; margin: 0; padding: 0; }
  html, body {
    width: 1200px; height: 900px; overflow: hidden;
    background: var(--backdrop);
    font-family: "Work Sans", sans-serif;
  }
  .stage {
    width: 1200px; height: 900px;
    display: flex; flex-direction: column; align-items: center; justify-content: center;
    gap: 40px;
  }
  .card {
    position: relative;
    width: 640px; height: 366px;
    background: var(--card);
    border: 1px solid var(--card-edge);
    box-shadow: 0 10px 30px rgba(0,0,0,.5);
    overflow: hidden;
  }
  .card-back .pattern {
    position: absolute; inset: 0;
    background: linear-gradient(135deg, #1e1e1e 0%, #262626 55%, #333 100%);
  }
  .card-back .wordmark {
    position: absolute; right: 70px; bottom: 66px;
    font-weight: 300; font-size: 30px; letter-spacing: 8px;
    color: var(--white);
  }
  .card-front {
    display: flex; align-items: center;
    background: linear-gradient(160deg, #191919 0%, #1d1d1d 60%, #262626 100%);
  }
  .brand {
    width: 290px; display: flex; flex-direction: column; align-items: center; gap: 18px;
  }
  .brand .mark { width: 22px; height: 22px; background: var(--gold); }
  .brand .wordmark {
    font-weight: 300; font-size: 30px; letter-spacing: 8px; color: var(--white);
  }
  .divider { width: 1px; height: 166px; background: var(--gold); }
  .contact { padding-left: 42px; color: var(--white); }
  .contact .name { font-weight: 600; font-size: 34px; color: var(--gold); line-height: 1.05; }
  .contact .role { font-weight: 400; font-size: 16px; margin: 4px 0 18px; letter-spacing: .5px; }
  .contact ul { list-style: none; display: flex; flex-direction: column; gap: 6px; }
  .contact li { display: flex; align-items: center; gap: 10px; font-size: 17px; letter-spacing: .6px; }
  .contact svg { width: 13px; height: 13px; flex: none; }
</style>
</head>
<body>
<main class="stage">
  <section class="card card-back">
    <div class="pattern" role="img" aria-label="Repeating embossed monogram pattern across the card back"></div>
    <span class="wordmark">BRIVETTA</span>
  </section>

  <section class="card card-front">
    <div class="brand">
      <span class="mark"></span>
      <span class="wordmark">BRIVETTA</span>
    </div>
    <div class="divider"></div>
    <div class="contact">
      <h1 class="name">Calvin Moross</h1>
      <p class="role">Co-Founder</p>
      <ul>
        <li>
          <svg viewBox="0 0 16 16" fill="none" stroke="#b3a37a" stroke-width="1.6"><path d="M4 1.5l2.5 3-1.5 1.8c.8 1.8 2 3 3.8 3.8L10.6 8.6l3 2.5-1.4 2.6C7 13.4 2.6 9 2.3 3.8z"/></svg>
          416-555-7391
        </li>
        <li>
          <svg viewBox="0 0 16 16" fill="none" stroke="#b3a37a" stroke-width="1.6"><rect x="4" y="1.5" width="8" height="13" rx="1.5"/><line x1="7" y1="12" x2="9" y2="12"/></svg>
          416-555-0186
        </li>
        <li>
          <svg viewBox="0 0 16 16" fill="none" stroke="#b3a37a" stroke-width="1.6"><rect x="1.5" y="3.5" width="13" height="9"/><path d="M1.5 3.5L8 9l6.5-5.5"/></svg>
          brivetta.ca Calvin@brivetta.ca
        </li>
      </ul>
    </div>
  </section>
</main>
</body>
</html>
```